Brisk Acre, LLC Web Design

I would like a web site design for a new lawn care business I am creating for my son. This is what it looks like now.

http://www.briskacrellc.example

Target Market(s)

Target customer is blue collar or middle class people who do not have time to do all of the grunt work around their home such as mowing the lawn, clearing snow etc. Or they need help moving or moving something such as mulch or wood. Shoot for an economical audience that may not have thought about having these tasks done for them.

Industry/Entity Type

Lawn Care

Colors
acd037
9bcb3c
cadf82
eaf2cf

Requirements
Must have
• I put in greens below. The colors that were available were not the best greens or the greens I would think about. The greens on the web site are more close.
Nice to have
• Will have a few more pictures of the logo guy on different machines. Will upload as soon as I get.

```html
<!DOCTYPE html>
<html lang="en">
<head>
<meta charset="utf-8">
<title>Brisk Acre, LLC</title>
<link href="https://fonts.googleapis.com/css2?family=PT+Sans:wght@400;700&family=PT+Sans+Narrow:wght@400;700&display=swap" rel="stylesheet">
<style>
:root{
  --green:#7cc21f;
  --green-light:#9bd23a;
  --green-dark:#3f8a10;
  --green-deep:#2e6e0b;
  --green-text:#2f7a12;
  --nav-text:#1f6e10;
  --white:#ffffff;
  --ink:#3a3a3a;
  --muted:#666;
  --line:#d9d9d9;
  --footer:#efefef;
  --brown:#4a2a1e;
}
*{margin:0;padding:0;box-sizing:border-box}
html,body{width:1024px;height:1200px;overflow:hidden}
body{position:relative;font-family:"PT Sans",sans-serif;background:var(--white);color:var(--ink)}
.abs{position:absolute}
.narrow{font-family:"PT Sans Narrow",sans-serif}

.hero-band{left:0;top:0;width:1024px;height:696px;
  background:radial-gradient(ellipse at 22% 0%,#d9f0a8 0%,rgba(160,214,70,.6) 14%,rgba(124,194,31,0) 32%),
  radial-gradient(ellipse at 50% 45%,#86c92a 0%,#74bd1e 60%,#6cb41a 100%);
  border-bottom:2px solid #5ea516}

.brand{left:136px;top:40px;display:flex;align-items:center;gap:10px}
.brand-dot{width:34px;height:34px;border-radius:50%;background:var(--green-deep)}
.brand-name{font-family:"PT Sans Narrow",sans-serif;font-weight:700;font-size:34px;color:var(--green-deep);line-height:1}

.callout{right:144px;top:44px;text-align:right;color:var(--white)}
.callout .lead{font-family:"PT Sans Narrow",sans-serif;font-size:15px}
.callout .lead b{font-weight:700}
.callout .phone{display:flex;align-items:center;justify-content:flex-end;gap:4px;margin-top:5px;font-family:"PT Sans Narrow",sans-serif;font-weight:700;font-size:30px;line-height:1}

.nav{left:136px;top:120px;width:752px;height:40px;border-radius:5px;
  background:linear-gradient(#ffffff,#ececec);box-shadow:0 1px 2px rgba(0,0,0,.25);display:flex;align-items:center}
.nav a{font-family:"PT Sans Narrow",sans-serif;font-weight:700;font-size:13px;color:var(--nav-text);text-decoration:none;position:absolute;top:0;height:40px;line-height:40px}
.nav .active{left:13px;width:78px;text-align:center;background:linear-gradient(#e4e4e4,#d3d3d3);border-top:2px solid var(--green-dark);line-height:38px}
.nav .active:after{content:"";position:absolute;left:34px;top:-1px;border:5px solid transparent;border-top-color:var(--green-dark)}

.hero-copy{left:149px;top:250px;width:340px;font-family:"PT Sans Narrow",sans-serif;font-weight:700;font-size:29px;line-height:35px;color:var(--white)}
.hero-copy em{font-style:normal;color:var(--green-deep)}
.btn-ghost{left:149px;top:378px;width:112px;height:36px;border-radius:3px;background:linear-gradient(#ffffff,#e9e9e9);box-shadow:0 1px 2px rgba(0,0,0,.25);
  font-family:"PT Sans Narrow",sans-serif;font-weight:700;font-size:14px;color:var(--green-text);text-align:center;line-height:36px}

.hero-media{left:512px;top:166px;width:312px;height:312px;border-radius:46% 46% 40% 40%;
  background:radial-gradient(ellipse at 50% 55%,#2d8a2a 0%,#3f9a2c 45%,rgba(110,180,30,0) 72%)}
.hero-rule{left:150px;top:500px;width:724px;height:4px;border-radius:50%;background:radial-gradient(ellipse,rgba(40,90,10,.45),rgba(40,90,10,0) 70%)}

.service{top:538px;width:240px;height:128px;border-radius:4px;overflow:hidden;background:var(--white);box-shadow:0 0 14px rgba(220,255,160,.6)}
.service .shot{height:92px}
.service .label{height:36px;display:flex;align-items:center;justify-content:space-between;padding:0 12px;font-family:"PT Sans Narrow",sans-serif;font-weight:700;font-size:14px;color:var(--brown)}
.shot-lawn{background:linear-gradient(100deg,#c83040 0%,#e44556 30%,#8fb04a 55%,#6f9a34 100%)}
.shot-snow{background:linear-gradient(180deg,#dfe3e6 0%,#c9cdd0 40%,#c8343c 62%,#a6262d 100%)}
.shot-yard{background:linear-gradient(120deg,#e23a2a 0%,#e8b22a 30%,#6f9a3c 55%,#8ab04e 100%)}

.about-photo{left:135px;top:730px;width:432px;height:151px;border-radius:4px;background:linear-gradient(90deg,#4a4a40 0%,#a8c43c 30%,#3d6a2a 55%,#c5d84a 80%,#3a3a36 100%)}
.about-title{left:135px;top:892px;font-family:"PT Sans Narrow",sans-serif;font-size:23px;color:var(--ink)}
.about-title span{color:#6aad1f}
.about-text{left:135px;top:926px;width:432px;font-size:11.6px;line-height:19.2px;color:var(--muted)}

.schedule{left:594px;top:729px;width:295px;height:316px;border:1px solid var(--line);background:var(--white)}
.schedule-head{height:64px;background:linear-gradient(#7cbf30,#5ea51b);display:flex;align-items:center;gap:8px;padding-left:22px;color:var(--white);font-family:"PT Sans Narrow",sans-serif;font-weight:700;font-size:20px}
.schedule-note{margin:16px 24px 0 24px;font-size:9px;line-height:13px;color:#555}
.field{position:absolute;left:22px;width:251px;height:27px;border:1px solid var(--line);font-size:10.5px;color:#777;line-height:25px;padding-left:9px;background:var(--white)}
.field .side{position:absolute;right:0;top:0;width:29px;height:25px;display:flex;align-items:center;justify-content:center}
.field .select-side{border-left:1px solid var(--line)}
.submit{position:absolute;left:22px;top:262px;width:251px;height:36px;background:linear-gradient(#8ccc45,#5ea51b);border:1px solid #4f9416;color:var(--white);font-weight:700;font-size:12.5px;text-align:center;line-height:34px}

.footer{left:0;top:1080px;width:1024px;height:92px;background:var(--footer);border-top:1px solid #ddd}
.footer-brand{left:140px;top:1105px;display:flex;align-items:center;gap:8px}
.footer-brand .brand-dot{width:26px;height:26px}
.footer-brand .brand-name{font-size:26px}
.links{font-size:10px;line-height:19.2px;color:#555;list-style:none}
.links li:before{content:"";display:inline-block;border:3px solid transparent;border-left:3px solid #555;margin-right:3px;vertical-align:0}
.contact-line{font-size:10px;line-height:19.2px;color:#555}
.social{top:1106px;width:26px;height:26px;border-radius:2px}
.bottom-bar{left:0;top:1172px;width:1024px;height:28px;background:#6aae1e;color:#234a0c;font-size:8.5px;line-height:28px}
</style>
</head>
<body>

<div class="abs hero-band"></div>

<div class="abs brand"><span class="brand-dot"></span><span class="brand-name">Brisk Acre, LLC</span></div>

<div class="abs callout">
  <div class="lead">Call Dale today for a <b>FREE</b> estimate</div>
  <div class="phone">
    <svg width="20" height="22" viewBox="0 0 20 22"><path d="M5 2 L8 6 L6 8 C7 11 9 13 12 14 L14 12 L18 15 L16 19 C9 19 3 13 2 5 Z" fill="none" stroke="#cfe9a0" stroke-width="1.6"/></svg>
    555-014-2700
  </div>
</div>

<nav class="abs nav">
  <a class="active" href="#">HOME</a>
  <a href="#" style="left:128px">LAWN CARE</a>
  <a href="#" style="left:213px">SNOW REMOVAL</a>
  <a href="#" style="left:325px">YARD CARE</a>
  <a href="#" style="left:414px">SCHEDULE</a>
  <a href="#" style="left:500px">CONTACT</a>
</nav>

<div class="abs hero-copy">We provide <em>cost effective and timely services</em> for Lawn Care, Snow Removal, and Yard Care.</div>
<div class="abs btn-ghost">CONTACT US</div>

<div class="abs hero-media" role="img" aria-label="Green and yellow zero-turn riding lawn mower"></div>
<div class="abs hero-rule"></div>

<div class="abs service" style="left:136px">
  <div class="shot shot-lawn" role="img" aria-label="Red push mower on freshly cut grass"></div>
  <div class="label">LAWN CARE SERVICES <svg width="12" height="12" viewBox="0 0 12 12"><path d="M1 6 H9 M5 2 L9 6 L5 10" stroke="#4a2a1e" stroke-width="2.2" fill="none"/></svg></div>
</div>
<div class="abs service" style="left:393px">
  <div class="shot shot-snow" role="img" aria-label="Red pickup truck fitted with a snow plow"></div>
  <div class="label">SNOW REMOVAL SERVICES <svg width="12" height="12" viewBox="0 0 12 12"><path d="M1 6 H9 M5 2 L9 6 L5 10" stroke="#4a2a1e" stroke-width="2.2" fill="none"/></svg></div>
</div>
<div class="abs service" style="left:648px">
  <div class="shot shot-yard" role="img" aria-label="Flower beds beside a curving green lawn"></div>
  <div class="label">YARD CARE SERVICES <svg width="12" height="12" viewBox="0 0 12 12"><path d="M1 6 H9 M5 2 L9 6 L5 10" stroke="#4a2a1e" stroke-width="2.2" fill="none"/></svg></div>
</div>

<div class="abs about-photo" role="img" aria-label="Two crew members in bright work shirts beside a riding mower in a garage"></div>
<h2 class="abs about-title">About <span>Brisk Acre LLC</span></h2>
<p class="abs about-text">Brisk Acre, LLC is the vision of Dale Ferrow, owner and main grunt. For the last 10 years he has been helping people by cutting their lawn, removing snow, cleaning yards or even just moving firewood, mulch or stones. He felt that it was time to take it to the next level and Brisk Acre, LLC was born. Brisk Acre, LLC is a locally owned business headquartered in Cedar Ridge. Dale takes personal pride in providing cost effective and timely services to his clients.</p>

<section class="abs schedule">
  <div class="schedule-head">
    <svg width="15" height="15" viewBox="0 0 15 15"><rect x="1" y="2" width="13" height="12" fill="none" stroke="#e8f5cf" stroke-width="1.4"/><path d="M1 5 H14 M4.5 5 V14 M7.5 5 V14 M10.5 5 V14 M1 8 H14 M1 11 H14" stroke="#e8f5cf" stroke-width="1"/></svg>
    SCHEDULE A SERVICE TODAY
  </div>
  <p class="schedule-note">Kindly enter your details and we will contact you soon for confirmation of your schedule.</p>
  <div class="field" style="top:117px">Lawn Care<span class="side select-side"><svg width="7" height="4"><path d="M0 0 H7 L3.5 4 Z" fill="#aaa"/></svg></span></div>
  <div class="field" style="top:152px">Name (required)</div>
  <div class="field" style="top:188px">Phone (required)</div>
  <div class="field" style="top:223px">Date of Appointment (required)<span class="side"><svg width="15" height="14" viewBox="0 0 15 14"><rect x=".5" y="1.5" width="14" height="12" fill="none" stroke="#999"/><path d="M.5 4.5 H14.5 M4 4.5 V13.5 M7.5 4.5 V13.5 M11 4.5 V13.5 M.5 7.5 H14.5 M.5 10.5 H14.5" stroke="#aaa" stroke-width=".8"/></svg></span></div>
  <div class="submit">Submit Form</div>
</section>

<div class="abs footer"></div>
<div class="abs footer-brand"><span class="brand-dot"></span><span class="brand-name">Brisk Acre, LLC</span></div>

<ul class="abs links" style="left:328px;top:1099px"><li>Home</li><li>Schedule</li><li>Contact</li></ul>
<ul class="abs links" style="left:393px;top:1099px"><li>Lawn Care</li><li>Snow Removal</li><li>Yard Care</li></ul>

<svg class="abs" style="left:520px;top:1105px" width="10" height="14" viewBox="0 0 10 14"><path d="M5 13 C2 9 1 7 1 5 A4 4 0 0 1 9 5 C9 7 8 9 5 13 Z" fill="#777"/><circle cx="5" cy="5" r="1.6" fill="#efefef"/></svg>
<div class="abs contact-line" style="left:536px;top:1099px">Company Name<br>48 Meadow Lane<br>Fairview, ST 00000</div>

<svg class="abs" style="left:648px;top:1104px" width="11" height="11" viewBox="0 0 20 22"><path d="M5 2 L8 6 L6 8 C7 11 9 13 12 14 L14 12 L18 15 L16 19 C9 19 3 13 2 5 Z" fill="#777"/></svg>
<svg class="abs" style="left:647px;top:1124px" width="12" height="9" viewBox="0 0 12 9"><rect width="12" height="9" fill="#777"/><path d="M0 0 L6 5 L12 0" stroke="#efefef" fill="none"/></svg>
<div class="abs contact-line" style="left:666px;top:1099px">555-014-2700<br>info@briskacre.example</div>

<div class="abs social" style="left:784px;background:#3b5d9c" role="img" aria-label="Social profile link"></div>
<div class="abs social" style="left:822px;background:#37a5d9" role="img" aria-label="Social profile link"></div>
<div class="abs social" style="left:860px;background:#2a72a6" role="img" aria-label="Social profile link"></div>

<div class="abs bottom-bar">
  <span style="position:absolute;left:142px">Copyright © 2014 - Brisk Acre LLC</span>
  <span style="position:absolute;right:138px">Sitemap | Privacy Policy</span>
</div>

</body>
</html>
```